Improve the UI for two Mobile Apps

Brevano licenses ERP software to mid-sized companies (50M plus). Brevano's product suite includes procurement, accounting and CRM applications.

We have two mobile Apps that integrate with our ERP applications - Tallyway Hub and Morrow Field Kit. The Tallyway Hub App allows a user to review and approve requisitions, purchase orders, supplier invoices and expense reports which are forwarded to the App from our ERP applications. The expense report App allows a user to enter travel expenses and attach photos of receipts.

We are satisfied with the functionality of both mobile Apps. Our goal is to improve the aesthetics (fonts, colors, graphics). We are looking for a clean, light weight, modern design. The design should also be consistent with our current Brevano colors (blue and green) and branding (see www.brevanosystems.com).

Documentation showing current screen shots for each App is attached (2 files).
Updates

Please focus on the 14 major forms in the attachment. The larger document includes about 40 forms. It is intended to illustrate the use of the Apps which hopefully is useful when considering design alternatives. We realize the budget may be insufficient for the complete redesign of both Apps. When accepting the final design we will negotiate a price for revising / completing all forms. At this point we will increase the project's budget or complete the remaining work in-house. Thanks, Derek...

Target Market(s)

We sell to mid-large sized corporations. Are primary customer is the purchasing agent.

Industry/Entity Type

Accounting

Number of Pages Required

5+ page

Requirements
Must have
• Clean, modern design of the major entry forms shown in the attached documents. I need graphics and colors only. Our developers will adjust the Apps. I have attached 2 sets of documents. The first 2 files illustrate the use of all forms in both apps. Several forms appear multiple times. The second set of 3 files include the unique forms in both apps (14 in total). These files are labeled "(major forms)".

```html
<!DOCTYPE html>
<html lang="en">
<head>
<meta charset="utf-8">
<title>Brevano – Edit Trip Info</title>
<link rel="stylesheet" href="https://fonts.googleapis.com/css2?family=Ubuntu:wght@400;500;700&display=swap">
<style>
  :root {
    --page-bg: #141414;
    --header-top: #3c3c3c;
    --header-bottom: #262626;
    --brand-blue: #1f7fd6;
    --title-text: #ffffff;
    --tab-green-top: #d2f58a;
    --tab-green-bottom: #8fd13c;
    --tab-blue-top: #3da4ea;
    --tab-blue-bottom: #1467c6;
    --panel-top: #3a9fe2;
    --panel-bottom: #0b58b2;
    --field-bg: #ffffff;
    --field-label: #5a5a5a;
    --button-top: #2d8ae0;
    --button-bottom: #0a3f8a;
    --button-text: #ffffff;
    --screen-code: #bdbdbd;
  }
  * { box-sizing: border-box; margin: 0; padding: 0; }
  html, body {
    width: 1200px;
    height: 2434px;
    overflow: hidden;
    background: var(--page-bg);
    font-family: "Ubuntu", sans-serif;
  }
  .screen { position: relative; width: 1200px; height: 2434px; }

  .app-header {
    position: absolute; left: 0; top: 0;
    width: 1200px; height: 368px;
    background: linear-gradient(var(--header-top), var(--header-bottom));
    display: flex; align-items: center; justify-content: center;
  }
  .brand-name {
    font-weight: 700;
    font-size: 150px;
    letter-spacing: 4px;
    color: var(--brand-blue);
    text-transform: uppercase;
    line-height: 1;
  }

  .page-title {
    position: absolute; left: 0; top: 420px; width: 1200px;
    text-align: center;
    font-weight: 500;
    font-size: 84px;
    color: var(--title-text);
  }

  .tab {
    position: absolute; top: 589px;
    width: 506px; height: 200px;
    border-radius: 38px 38px 0 0;
    padding-top: 56px;
    text-align: center;
    font-size: 50px;
    color: #ffffff;
  }
  .tab-description {
    left: 56px;
    background: linear-gradient(var(--tab-green-top), var(--tab-green-bottom));
  }
  .tab-accounting {
    left: 589px;
    background: linear-gradient(var(--tab-blue-top), var(--tab-blue-bottom));
    border: 3px solid #0d4f9c;
    border-bottom: none;
  }

  .form-panel {
    position: absolute; left: 56px; top: 761px;
    width: 1088px; height: 1508px;
    border-radius: 38px;
    background: linear-gradient(var(--panel-top), var(--panel-bottom));
    box-shadow: 0 4px 10px rgba(0,0,0,0.5);
  }
  .field {
    position: absolute; left: 49px;
    width: 979px; height: 161px;
    border-radius: 52px;
    background: var(--field-bg);
    display: flex; align-items: center;
    padding-left: 49px;
    font-size: 42px;
    color: var(--field-label);
  }
  .submit-button {
    position: absolute; left: 300px; top: 1305px;
    width: 461px; height: 105px;
    border-radius: 52px;
    background: linear-gradient(var(--button-top), var(--button-bottom));
    border: 3px solid #083470;
    display: flex; align-items: center; justify-content: center;
    font-size: 50px;
    color: var(--button-text);
    letter-spacing: 1px;
  }

  .screen-code {
    position: absolute; right: 56px; top: 2318px;
    font-size: 40px;
    color: var(--screen-code);
  }
</style>
</head>
<body>
<main class="screen">
  <header class="app-header">
    <span class="brand-name">Brevano</span>
  </header>

  <h1 class="page-title">Edit Trip Info</h1>

  <div class="tab tab-description">Description</div>
  <div class="tab tab-accounting">Accounting</div>

  <section class="form-panel">
    <div class="field" style="top:143px">Corporate Card</div>
    <div class="field" style="top:357px">Project</div>
    <div class="field" style="top:597px">Entity</div>
    <div class="field" style="top:825px">Division</div>
    <div class="field" style="top:1039px">Cost Center</div>
    <div class="submit-button">SUBMIT</div>
  </section>

  <div class="screen-code">C5</div>
</main>
</body>
</html>
```